help me Create Marigold Table Catering offsite menus

I need something vibrant and it needs some pictures to go with the food i will include the logo of the location and the menu. it is for offsite catering to be delivered to venues in our local town, we are currently catering in house only but are expanding to do delivery so need something that i can use as a menu. the file needs to be able to be edited

Target Market(s)

local small businesses that require catering for their group lunches

Industry/Entity Type

Catering

Font styles to use
Serif
Decorative

Requirements
Must have
• colour and soul, must have a good feeling and be happy
Nice to have
• some other stock photos of the described products
Should not have
• not be too corporate and businessy

```html
<!DOCTYPE html>
<html lang="en">
<head>
<meta charset="utf-8">
<title>Marigold Table Catering – Offsite Menus</title>
<link rel="stylesheet" href="https://fonts.googleapis.com/css2?family=Almendra:wght@400;700&family=Pathway+Gothic+One&family=Lora:wght@700&display=swap">
<style>
  :root{
    --backdrop:#3b3833;
    --frame:#0e1319;
    --panel:#121a23;
    --orange:#e8702a;
    --orange-dark:#c9561a;
    --navy:#16314a;
    --ink:#e9e6df;
    --muted:#b9b4aa;
    --rule:#c8c23a;
    --marigold:#f2a33a;
  }
  *{box-sizing:border-box;margin:0;padding:0}
  html,body{width:1200px;height:754px;overflow:hidden;background:var(--backdrop)}
  .canvas{position:relative;width:1200px;height:754px}
  .page{position:absolute;top:27px;width:540px;height:700px;background:var(--frame);padding:8px}
  .page--platter{left:40px}
  .page--tea{left:620px}
  .page__panel{position:relative;width:100%;height:100%;background:var(--panel);
    clip-path:polygon(14px 0,calc(100% - 14px) 0,100% 14px,100% calc(100% - 14px),calc(100% - 14px) 100%,14px 100%,0 calc(100% - 14px),0 14px)}
  .abs{position:absolute}
  .brand{position:absolute;border-radius:50%;background:var(--navy);display:flex;align-items:center;justify-content:center;text-align:center;
    font-family:"Almendra",serif;font-weight:700;color:var(--ink);line-height:1.05}
  .photo{position:absolute;background:radial-gradient(circle at 40% 40%,#e9d9b8,#b98a55 60%,#5a3b22)}
  .photo--round{border-radius:50%}
  .ribbon{position:absolute;background:var(--orange);color:#fff;display:flex;align-items:center;justify-content:center;
    font-family:"Almendra",serif;font-weight:700;letter-spacing:.5px;
    clip-path:polygon(0 0,100% 0,96% 50%,100% 100%,0 100%,4% 50%)}
  .item{position:absolute;font-family:"Pathway Gothic One",sans-serif;color:var(--ink);text-transform:uppercase;letter-spacing:.3px;white-space:nowrap}
  .item small{display:block;font-size:7.5px;color:var(--muted);margin-top:2px}
  .price{position:absolute;font-family:"Pathway Gothic One",sans-serif;color:var(--ink);white-space:nowrap}
  .rule{position:absolute;width:1.5px}
  .salad-word{font-family:"Almendra",serif;font-weight:700;color:#fff;font-size:21px;transform:rotate(-12deg)}
  .lunch-desc{font-family:"Lora",serif;font-weight:700;color:var(--ink);font-size:8px;line-height:14px;text-align:center}
  .phone{font-family:"Lora",serif;font-size:15px;color:#fff;display:flex;align-items:center;gap:8px}
  .booking{font-family:"Lora",serif;font-size:8px;color:var(--ink);white-space:nowrap}
</style>
</head>
<body>
<div class="canvas">

  <!-- Platter & lunch menu -->
  <section class="page page--platter">
    <div class="page__panel">
      <div class="brand" style="left:33px;top:14px;width:112px;height:112px;font-size:15px">Marigold<br>Table<br>Catering</div>
      <div class="photo" role="img" aria-label="Sliced red capsicum" style="left:190px;top:19px;width:97px;height:84px;border-radius:45%;background:radial-gradient(circle,#3a0a08 30%,#d8261a 55%,#8e1209)"></div>
      <div class="abs salad-word" style="left:304px;top:40px">Salad</div>
      <div class="photo photo--round" role="img" aria-label="Plate of caprese salad with tomato, mozzarella and basil" style="left:382px;top:19px;width:104px;height:104px;background:radial-gradient(circle,#e8e3d8 30%,#d24a34 55%,#f3f1ec 75%)"></div>

      <div class="ribbon" style="left:38px;top:130px;width:462px;height:35px;font-size:15px">Platter menu</div>

      <div class="item" style="left:61px;top:190px;font-size:10.5px">Hot finger food platter (chef's choice 60 pieces)</div>
      <div class="price" style="left:414px;top:190px;font-size:10.5px">$105.00</div>

      <div class="item" style="left:61px;top:215px;font-size:10.5px">Hot roast buffet platter pork or beef with roast vegetables<small>&amp; one grazing salad minimum 10 guests</small></div>
      <div class="price" style="left:414px;top:215px;font-size:10.5px">$16.50PP</div>

      <div class="item" style="left:61px;top:254px;font-size:10.5px">Sandwich box (10 rounds)</div>
      <div class="price" style="left:414px;top:254px;font-size:10.5px">$68.00</div>

      <div class="item" style="left:61px;top:279px;font-size:10.5px">Medium bread roll platter 15 medium size lunch rolls</div>
      <div class="price" style="left:414px;top:279px;font-size:10.5px">$75.00</div>

      <div class="item" style="left:61px;top:304px;font-size:10.5px">Large meat and salad rolls<small>(choice of chicken, chicken schnitzel, roast beef, ham)</small></div>
      <div class="price" style="left:404px;top:304px;font-size:10.5px">$9.00 EACH</div>

      <div class="item" style="left:61px;top:344px;font-size:10.5px">Wraps<small>(choice of chicken, chicken schnitzel, roast beef, ham)</small></div>
      <div class="price" style="left:404px;top:344px;font-size:10.5px">$7.50 EACH</div>

      <div class="item" style="left:61px;top:384px;font-size:10.5px">Individual salad bowls – ceasar, greek, creamy pasta, seafood<small>add chicken or chilled chicken schnitzel</small></div>
      <div class="price" style="left:426px;top:384px;font-size:10.5px">$9.50</div>
      <div class="price" style="left:428px;top:399px;font-size:8px;color:var(--muted)">$3.50</div>

      <div class="item" style="left:61px;top:426px;font-size:10.5px">Large grazing salads &nbsp;add one to a sandwich platter<small>or hot finger food platter add a healthy side for your group (serves 10)</small></div>
      <div class="price" style="left:420px;top:426px;font-size:10.5px">$35.00</div>

      <div class="item" style="left:61px;top:467px;font-size:10.5px">Pizza, pasta and salad (minimum 8 guests)</div>
      <div class="price" style="left:414px;top:467px;font-size:10.5px">$19.00PP</div>

      <div class="rule" style="left:475px;top:186px;height:227px;background:var(--rule)"></div>

      <div class="photo photo--round" role="img" aria-label="Buffet trays of sandwiches and chicken salad" style="left:16px;top:491px;width:158px;height:158px"></div>

      <div class="ribbon" style="left:186px;top:505px;width:297px;height:38px;font-size:19px">Lunch</div>
      <div class="item" style="left:213px;top:558px;font-size:15px">Gazing table minimum 5</div>
      <div class="price" style="left:404px;top:558px;font-size:15px">$16.50 PP</div>
      <div class="abs lunch-desc" style="left:185px;top:584px;width:300px">Make your own sandwich buffet for guests to make their own sandwich from a variety of breads and fillings with tea and coffee facilities.</div>

      <div class="abs phone" style="left:380px;top:627px">
        <svg width="12" height="12" viewBox="0 0 24 24" aria-hidden="true"><path fill="none" stroke="#fff" stroke-width="2" d="M6.6 10.8a15 15 0 0 0 6.6 6.6l2.2-2.2a1 1 0 0 1 1-.25 11.4 11.4 0 0 0 3.6.6 1 1 0 0 1 1 1V20a1 1 0 0 1-1 1A17 17 0 0 1 3 4a1 1 0 0 1 1-1h3.5a1 1 0 0 1 1 1c0 1.25.2 2.45.6 3.6a1 1 0 0 1-.25 1z"/></svg>
        02 5550 4817
      </div>
      <div class="abs booking" style="left:150px;top:650px">To book in your event call us now on 02 5550 4817 or go to www.marigoldtable.com.au</div>
    </div>
  </section>

  <!-- Tea, coffee & morning tea menu -->
  <section class="page page--tea">
    <div class="page__panel">
      <div class="photo" role="img" aria-label="Stack of chocolate chip cookies" style="left:42px;top:46px;width:210px;height:100px;border-radius:50%;background:radial-gradient(ellipse,#c98a45 40%,#9a5d25 70%,transparent 72%)"></div>
      <div class="brand" style="left:291px;top:22px;width:184px;height:156px;font-size:21px">Marigold<br>Table<br>Catering</div>

      <div class="ribbon" style="left:44px;top:200px;width:199px;height:26px;font-size:12.5px">Tea &amp; Coffee</div>
      <div class="item" style="left:64px;top:246px;font-size:9.5px">Tea and coffee station<small style="font-size:5px">Self serve station refreshed through the whole day</small></div>
      <div class="price" style="left:202px;top:246px;font-size:9.5px">$3.00PP</div>
      <div class="item" style="left:64px;top:271px;font-size:9.5px">Barrista delivered<small style="font-size:5px">(pre order only)</small></div>
      <div class="price" style="left:197px;top:271px;font-size:9.5px">$5.50 EACH</div>
      <div class="rule" style="left:242px;top:246px;height:33px;background:var(--ink)"></div>

      <div class="ribbon" style="left:44px;top:311px;width:199px;height:26px;font-size:12.5px">Extra</div>
      <div class="item" style="left:64px;top:357px;font-size:9.5px">Juice 2 LT bottle</div>
      <div class="price" style="left:202px;top:357px;font-size:9.5px">$3.95</div>
      <div class="rule" style="left:242px;top:359px;height:8px;background:var(--ink)"></div>

      <div class="photo" role="img" aria-label="Catering platter of pastries set out in a bright function room" style="left:286px;top:200px;width:186px;height:171px;background:linear-gradient(180deg,#8fa3ad 0%,#5d6a6c 45%,#b98a55 75%,#6b4528 100%)"></div>

      <div class="ribbon" style="left:44px;top:394px;width:440px;height:30px;font-size:14px">Morning or Afternoon Tea</div>

      <div class="item" style="left:106px;top:451px;font-size:10.5px">Scones and slices platter</div>
      <div class="price" style="left:329px;top:451px;font-size:10.5px">$6.50 PER PERSON</div>
      <div class="item" style="left:106px;top:477px;font-size:10.5px">Muffins</div>
      <div class="price" style="left:329px;top:477px;font-size:10.5px">$5.00 PER PERSON</div>
      <div class="item" style="left:106px;top:507px;font-size:10.5px">Homemade biscuits</div>
      <div class="price" style="left:329px;top:507px;font-size:10.5px">$4.50 PER PERSON</div>
      <div class="item" style="left:106px;top:533px;font-size:10.5px">Banana bread</div>
      <div class="price" style="left:329px;top:533px;font-size:10.5px">$6.00 PER PERSON</div>
      <div class="item" style="left:106px;top:564px;font-size:10.5px">Gluten free frittata</div>
      <div class="price" style="left:329px;top:564px;font-size:10.5px">$5.50 PER PERSON</div>
      <div class="item" style="left:106px;top:590px;font-size:10.5px">Ploughmans platter</div>
      <div class="price" style="left:329px;top:590px;font-size:10.5px">$8.50 PER PERSON</div>
      <div class="item" style="left:106px;top:621px;font-size:10.5px">Whole fresh fruit platter</div>
      <div class="price" style="left:329px;top:621px;font-size:10.5px">$45.00 PER PLATTER</div>
      <div class="item" style="left:106px;top:646px;font-size:10.5px">Chopped fresh seasonal fruit platter</div>
      <div class="price" style="left:329px;top:646px;font-size:10.5px">$49.50 PER PLATTER</div>
      <div class="rule" style="left:439px;top:445px;height:206px;background:var(--ink)"></div>
    </div>
  </section>

</div>
</body>
</html>
```